Vemtri Gymnastics Silver gym banner

We need a banner for our new gym.
It should have navy, light blue, lilac and purple colors with our name, logo and other wording in navy color. Colors should bleed one into the other.
File with name, logo and other wording is attached.
Words: Rhythmic gymnastics, ballet, etc should be on the bottom

Target Market(s)

Girls 3 to 16 years of age

Industry/Entity Type

Athletics

Font styles to use
Other font styles liked:
• Please use fonts on file included

Colors
0054AA
0677BA
7BADD7
CADEEF
E8F1F8
0094D4
00A9DD
6FCCEA
C7EBF8
E9F6FB
00AB8E
00BBA5
67D7C9
C6EFE9
E9F9F6
6B429C
8869AF
B7A5CE
E3DAEB
F3F0F8

Requirements
Must have
• our logo and name of the gym
Nice to have
• rhythmic gymnastics feel
Should not have
• bold colors

```html
<!DOCTYPE html>
<html lang="en">
<head>
<meta charset="utf-8">
<title>Vemtri Gymnastics – School of Champions Banner</title>
<link rel="stylesheet" href="https://fonts.googleapis.com/css2?family=Poppins:wght@600;700&display=swap">
<style>
  :root {
    --backdrop: #bdbdbd;
    --banner-bg: #ffffff;
    --navy: #0054aa;
    --purple: #6b429c;
    --lilac: #b7a5ce;
    --lilac-soft: #e3daeb;
    --sky: #c7ebf8;
    --sky-mid: #7badd7;
  }
  * { margin: 0; padding: 0; box-sizing: border-box; }
  html, body {
    width: 793px;
    height: 1200px;
    overflow: hidden;
    background: var(--backdrop);
    font-family: "Poppins", sans-serif;
  }
  .banner {
    position: absolute;
    left: 30px;
    top: 347px;
    width: 733px;
    height: 505px;
    background: var(--banner-bg);
    overflow: hidden;
    box-shadow: 4px 6px 10px rgba(0, 0, 0, 0.25);
  }
  .athletes-photo {
    position: absolute;
    left: 0;
    top: 0;
    width: 733px;
    height: 505px;
  }
  .brand {
    position: absolute;
    left: 44px;
    top: 50px;
    display: flex;
    align-items: center;
    gap: 12px;
  }
  .brand-dot {
    width: 40px;
    height: 40px;
    border-radius: 50%;
    background: var(--navy);
  }
  .brand-name {
    font-weight: 600;
    font-size: 28px;
    color: var(--navy);
    letter-spacing: -0.3px;
  }
  .headline {
    position: absolute;
    left: 40px;
    top: 126px;
    font-weight: 700;
    line-height: 0.86;
    letter-spacing: -1.5px;
  }
  .headline-top {
    display: block;
    font-size: 68px;
    color: var(--navy);
  }
  .headline-accent {
    display: block;
    font-size: 80px;
    color: var(--purple);
  }
  .class-list {
    position: absolute;
    left: 0;
    top: 281px;
    list-style: none;
  }
  .class-item {
    width: 274px;
    height: 32px;
    margin-bottom: 4px;
    background: var(--lilac);
    clip-path: polygon(0 0, 100% 0, 95% 50%, 100% 100%, 0 100%);
    padding-left: 45px;
    font-weight: 600;
    font-size: 17px;
    line-height: 32px;
    color: var(--navy);
  }
</style>
</head>
<body>
  <div class="banner">
    <svg class="athletes-photo" viewBox="0 0 733 505" role="img" aria-label="Photo of three young gymnasts: one on aerial silks, one in a standing split holding a ribbon, one seated in a split">
      <defs>
        <linearGradient id="athletes-tones" x1="0" y1="0" x2="0.35" y2="1">
          <stop offset="0" stop-color="#c7ebf8"/>
          <stop offset="0.45" stop-color="#e3daeb"/>
          <stop offset="0.75" stop-color="#b7a5ce"/>
          <stop offset="1" stop-color="#7badd7"/>
        </linearGradient>
      </defs>
      <path d="M560 0 H690 C705 120 715 260 700 420 L690 470 C600 480 420 480 275 465 C300 420 360 330 470 300 C520 280 545 200 545 120 Z" fill="url(#athletes-tones)" opacity="0.75"/>
    </svg>

    <div class="brand">
      <span class="brand-dot"></span>
      <span class="brand-name">Vemtri Gymnastics</span>
    </div>

    <h1 class="headline">
      <span class="headline-top">SCHOOL OF</span>
      <span class="headline-accent">CHAMPIONS</span>
    </h1>

    <ul class="class-list">
      <li class="class-item">Rhythmic Gymnastics</li>
      <li class="class-item">Ballroom Dance</li>
      <li class="class-item">Ballet</li>
      <li class="class-item">Stretching</li>
      <li class="class-item">Hip Hop</li>
    </ul>
  </div>
</body>
</html>
```